Bright Tooth Dentistry Business Card

We need business cards for our dental office.
We are looking for a clean, elegant design

We provide dental services to children.
Our card needs to be appealing to referring dentists, parents and our team

Target Market(s)

referring dentists, parents and our team

Industry/Entity Type

Dental Clinic

Contact Information for Business Card

4816 Juniper Lane, Suite 100
Cedar Hollow, PA 15237

412-837-2961 Voice
412-837-2962 fax
info@brighttoothdentalpa.com email
www.brighttoothdentalpa.com web

Font styles to use
Sans Serif

Requirements
Must have
• White background - clean, crisp, elegant, simple
• rounded corners
• different color palate - once we come up with design, we will replace the blue with orange, green,
Nice to have
• Follow our logo typeface and colors
• then we can replace color

```html
<!DOCTYPE html>
<html lang="en">
<head>
<meta charset="utf-8">
<title>Bright Tooth Dentistry – Business Card</title>
<link rel="stylesheet" href="https://fonts.googleapis.com/css2?family=Arimo:wght@400;700&family=Noto+Serif:wght@400&display=swap">
<style>
  :root {
    --brand-blue: #1ea8e4;
    --brand-grey: #8f9093;
    --ink: #3f3f3f;
    --card-bg: #ffffff;
    --page-bg: #ececec;
    --dot-blue: #2aa9e0;
  }
  * { box-sizing: border-box; margin: 0; padding: 0; }
  html, body { width: 1200px; height: 1200px; overflow: hidden; background: var(--page-bg); }
  .sheet { position: relative; width: 1200px; height: 1200px; }

  .card {
    position: absolute;
    left: 130px;
    width: 930px;
    height: 510px;
    background: var(--card-bg);
    border-radius: 34px;
    box-shadow: 0 6px 18px rgba(0,0,0,0.12);
    overflow: hidden;
  }
  .card--appointment { top: 63px; font-family: "Noto Serif", Georgia, serif; color: var(--ink); }
  .card--contact { top: 630px; font-family: "Arimo", Arial, sans-serif; }

  .abs { position: absolute; }

  /* Appointment side */
  .appt-title { left: 73px; top: 112px; font-size: 27px; font-weight: 400; }
  .brand-name--small {
    right: 66px; top: 112px;
    font-family: "Arimo", Arial, sans-serif;
    font-weight: 700; font-size: 31px; color: var(--brand-blue);
  }
  .field-row {
    left: 73px; right: 66px; display: flex; align-items: flex-end;
    font-size: 24px; gap: 10px;
  }
  .dots { flex: 1; border-bottom: 3px dotted var(--dot-blue); height: 1px; margin-bottom: 7px; }
  .dots--date { flex: 0 0 355px; }
  .dots--time { flex: 0 0 140px; }
  .row-name { top: 176px; }
  .row-date { top: 222px; }
  .row-note { top: 346px; }
  .rule-dotted { left: 66px; right: 66px; top: 405px; border-bottom: 3px dotted var(--dot-blue); }

  .day-picker {
    left: 92px; right: 84px; top: 298px;
    display: flex; justify-content: space-between; align-items: center;
    font-size: 23px;
  }
  .day { display: flex; align-items: center; gap: 12px; }
  .day-box { width: 42px; height: 32px; border: 3px solid var(--brand-blue); }

  .appt-footer {
    left: 0; right: 0; top: 420px; text-align: center;
    font-size: 23px; line-height: 30px;
  }

  /* Contact side */
  .brand-name--large {
    left: 68px; top: 168px;
    font-weight: 700; font-size: 46px; color: var(--brand-blue);
  }
  .person { right: 47px; top: 310px; text-align: right; }
  .person-name { font-size: 34px; font-weight: 700; line-height: 38px; }
  .person-first { color: var(--brand-blue); }
  .person-last { color: var(--brand-grey); }
  .person-title { font-size: 19px; color: #555; line-height: 20px; }
  .divider { left: 51px; right: 47px; top: 389px; border-top: 2px solid var(--brand-blue); }

  .contact-list { left: 52px; top: 402px; list-style: none; font-size: 18px; color: #444; }
  .contact-list li { display: flex; align-items: center; height: 26px; gap: 12px; }
  .contact-list svg { width: 20px; height: 18px; fill: var(--brand-blue); }

  .address { right: 47px; top: 403px; text-align: right; font-size: 18px; color: #444; line-height: 25px; font-style: normal; }
  .web { font-size: 17px; color: #333; margin-top: 2px; }
  .web-highlight { color: var(--brand-blue); }
</style>
</head>
<body>
<main class="sheet">

  <section class="card card--appointment" aria-label="Appointment card">
    <h2 class="abs appt-title">Next Appointment</h2>
    <div class="abs brand-name--small">Bright Tooth Dentistry</div>

    <div class="abs field-row row-name"><span>Name:</span><span class="dots"></span></div>
    <div class="abs field-row row-date">
      <span>Date:</span><span class="dots dots--date"></span>
      <span>Time:</span><span class="dots dots--time"></span><span>AM/PM</span>
    </div>

    <div class="abs day-picker">
      <span class="day">Sun<span class="day-box"></span></span>
      <span class="day">Mon<span class="day-box"></span></span>
      <span class="day">Tue<span class="day-box"></span></span>
      <span class="day">Wed<span class="day-box"></span></span>
      <span class="day">Thu<span class="day-box"></span></span>
      <span class="day">Fri<span class="day-box"></span></span>
      <span class="day">Sat<span class="day-box"></span></span>
    </div>

    <div class="abs field-row row-note"><span>Note:</span><span class="dots"></span></div>
    <div class="abs rule-dotted"></div>

    <p class="abs appt-footer">If you are unable to keep your appointment<br>Please contact us as soon as possible</p>
  </section>

  <section class="card card--contact" aria-label="Contact card">
    <div class="abs brand-name--large">Bright Tooth Dentistry</div>

    <div class="abs person">
      <div class="person-name"><span class="person-first">Daniel</span> <span class="person-last">Reyes</span></div>
      <div class="person-title">President</div>
    </div>

    <div class="abs divider"></div>

    <ul class="abs contact-list">
      <li>
        <svg viewBox="0 0 24 24" aria-hidden="true"><path d="M6.6 10.8a15.1 15.1 0 0 0 6.6 6.6l2.2-2.2c.3-.3.7-.4 1-.2 1.1.4 2.3.6 3.6.6.6 0 1 .4 1 1V20c0 .6-.4 1-1 1C10.6 21 3 13.4 3 4c0-.6.4-1 1-1h3.5c.6 0 1 .4 1 1 0 1.3.2 2.5.6 3.6.1.3 0 .7-.2 1z"/></svg>
        <span>412-837-2961</span>
      </li>
      <li>
        <svg viewBox="0 0 24 24" aria-hidden="true"><path d="M6 2h12v5H6zM3 8h18a2 2 0 0 1 2 2v7h-5v5H6v-5H1v-7a2 2 0 0 1 2-2zm5 8v4h8v-4z"/></svg>
        <span>412-837-2962</span>
      </li>
      <li>
        <svg viewBox="0 0 24 24" aria-hidden="true"><path d="M2 5h20v14H2zm2 2v.5l8 5.5 8-5.5V7zm0 2.9V17h16V9.9l-8 5.5z"/></svg>
        <span>info@brighttoothdentalpa.com</span>
      </li>
    </ul>

    <address class="abs address">
      4816 Juniper Lane, Suite 240 Cedar<br>
      Hollow, PA 15237
      <div class="web">www.<span class="web-highlight">brighttoothdentalpa</span>.com</div>
    </address>
  </section>

</main>
</body>
</html>
```